NEED Homepage Website Design for Event Planning Business

We need a homepage mockup for an event planning company based in Massachusetts. We provide a custom trailer to rent along with chairs, tables, lighting, etc.

Please add a "Check Availability" call to action which is just a form
- First & Last Name
- Phone
- Email Address
- Date Request

Add an PICTURELY section (use attached photos as we do not even have an IG account yet)

1 page

```html
<!DOCTYPE html>
<html lang="en">
<head>
<meta charset="utf-8">
<title>Hearthside Events — Home</title>
<link href="https://fonts.googleapis.com/css2?family=Fira+Sans:wght@400;500;600;700&family=Roboto:wght@400;500;700&display=swap" rel="stylesheet">
<style>
:root{
  --accent:#ef4423;
  --ink:#1d1d1d;
  --text:#333333;
  --white:#ffffff;
  --paper:#f1efee;
  --panel:rgba(20,20,20,.82);
  --footer:#262626;
  --rule:#9a9a9a;
}
*{box-sizing:border-box;margin:0;padding:0}
html,body{width:1200px;height:3882px;overflow:hidden}
body{font-family:"Roboto",sans-serif;color:var(--text);background:var(--white);position:relative}
.heading{font-family:"Fira Sans",sans-serif;color:var(--ink)}
.btn{display:inline-block;background:var(--accent);color:var(--white);font-family:"Fira Sans",sans-serif;font-weight:700;text-transform:uppercase;letter-spacing:.3px}
.photo{display:block}

/* Header */
.site-header{position:absolute;top:0;left:0;width:1200px;height:113px;background:var(--white)}
.brand{position:absolute;left:132px;top:30px;font-family:"Fira Sans",sans-serif;font-weight:700;font-size:30px;color:var(--ink);letter-spacing:.5px;display:flex;align-items:center;gap:10px}
.brand-mark{width:14px;height:14px;background:var(--ink)}
.follow{position:absolute;left:714px;top:27px;display:flex;align-items:center;gap:8px;font-size:12px;color:var(--text)}
.social-dot{width:26px;height:26px;border-radius:50%;background:#1c5fb8}
.social-dot.sky{background:#1f9ce8}
.social-dot.navy{background:#1a3b7d}
.call{position:absolute;left:914px;top:22px;display:flex;align-items:center;gap:12px}
.call-text small{display:block;font-size:11px;color:var(--text)}
.call-text strong{font-size:19px;font-weight:500;color:var(--ink);letter-spacing:.5px}
.main-nav{position:absolute;right:130px;top:77px;display:flex;gap:39px;font-size:15px;color:var(--ink)}
.main-nav .active{color:var(--accent);font-weight:700;text-decoration:underline;text-underline-offset:5px}

/* Hero */
.hero{position:absolute;top:113px;left:0;width:1200px;height:570px}
.hero .photo{width:100%;height:100%;background:linear-gradient(120deg,#3a4d3a 0%,#5c6b73 35%,#dcdcd6 60%,#4a5357 80%,#3b4a34 100%)}
.booking{position:absolute;left:120px;top:95px;width:355px;height:350px;background:var(--panel);padding:32px 30px}
.booking h2{color:var(--white);font-size:21px;font-weight:600;margin-bottom:18px}
.field-row{display:flex;gap:11px}
.field{height:33px;background:var(--white);margin-bottom:12px;font-size:10px;color:var(--ink);padding:10px 14px;flex:1}
.booking .btn{width:100%;height:42px;font-size:16px;text-align:center;line-height:42px;margin-top:6px}
.dots{position:absolute;left:548px;top:518px;display:flex;gap:15px}
.dots span{width:9px;height:9px;border-radius:50%;background:var(--white)}
.dots .on{background:var(--accent)}

/* Welcome */
.welcome{position:absolute;top:683px;left:0;width:1200px;height:538px}
.welcome-copy{position:absolute;left:131px;top:68px;width:425px}
.eyebrow{font-size:18px;color:var(--ink);font-family:"Fira Sans",sans-serif}
.welcome-copy h1{font-size:29px;font-weight:500;margin-top:4px}
.rule{width:135px;height:2px;background:var(--rule);margin:16px 0 28px}
.welcome-copy p{font-size:15.5px;line-height:23.5px;color:var(--ink);margin-bottom:24px}
.welcome-copy .btn{font-size:13px;padding:8px 13px;margin-top:6px}
.welcome .photo{position:absolute;left:588px;top:48px;width:481px;height:437px;background:linear-gradient(160deg,#eae8e2 0%,#c8b59a 40%,#4e5a3d 75%,#2e2e2e 100%)}

/* Rental */
.rental{position:absolute;top:1221px;left:0;width:1200px;height:962px;background:var(--paper)}
.section-title{text-align:center;font-size:23px;font-weight:600;letter-spacing:.4px}
.rental .section-title{margin-top:45px}
.mini-rule{width:36px;height:2px;background:var(--rule);margin:8px auto 0}
.rental-grid{position:absolute;left:131px;top:124px;width:939px;display:grid;grid-template-columns:451px 451px;column-gap:37px;row-gap:41px}
.rental-card .photo{height:238px}
.rental-card h3{font-size:13px;font-weight:700;margin-top:30px;letter-spacing:.2px}
.rental-card p{font-size:12px;line-height:18px;color:var(--ink);margin-top:8px;width:300px}
.rental-card .btn{font-size:10.5px;padding:6px 12px;margin-top:10px}
.ph-trailer{background:linear-gradient(135deg,#e8e8e6,#9b8f7c 55%,#5f6a55)}
.ph-barrels{background:linear-gradient(180deg,#5f86b8 0%,#9fb6cc 30%,#6d4a2a 55%,#3b2414 100%)}
.ph-tent{background:radial-gradient(ellipse at 50% 65%,#f3c38a 0%,#b07a47 30%,#1e2a3a 70%,#0f1622 100%)}
.ph-lights{background:linear-gradient(160deg,#4f5b66 0%,#e3e3de 50%,#5a6040 100%)}

/* Packages */
.packages{position:absolute;top:2183px;left:0;width:1200px;height:595px}
.packages .photo{position:absolute;left:131px;top:54px;width:529px;height:476px;background:linear-gradient(170deg,#f2f1ec 0%,#b9b6ae 35%,#6d6a5f 65%,#8a8478 100%)}
.packages-copy{position:absolute;left:704px;top:80px;width:370px}
.packages-copy h2{font-size:23px;font-weight:600;letter-spacing:.3px}
.packages-copy .rule{width:72px;margin:14px 0 38px}
.package-list{list-style:none}
.package-list li{position:relative;padding-left:32px;width:325px;font-size:15.5px;line-height:24px;color:var(--ink);margin-bottom:31px}
.package-list li::before{content:"";position:absolute;left:6px;top:8px;width:7px;height:7px;border-right:1.5px solid var(--ink);border-top:1.5px solid var(--ink);transform:rotate(45deg)}
.package-list strong{font-weight:700}

/* FAQ */
.faq{position:absolute;top:2778px;left:0;width:1200px;height:388px;background:linear-gradient(180deg,#3b3f42,#2f3a33)}
.faq .section-title{color:var(--white);margin-top:50px}
.faq .mini-rule{background:var(--white)}
.faq-card{position:absolute;left:167px;top:125px;width:876px;height:213px;background:var(--white);padding:45px 54px}
.faq-card h3{font-size:14px;font-weight:700;letter-spacing:.3px}
.faq-card p{font-size:13.5px;line-height:20px;color:var(--ink);margin-top:18px}

/* Photo feed */
.photo-feed{position:absolute;top:3166px;left:0;width:1200px;height:374px}
.photo-feed .section-title{position:absolute;top:83px;width:100%}
.feed-strip{position:absolute;left:7px;top:144px;display:flex;gap:10px}
.feed-strip .photo{width:230px;height:217px}
.feed-a{background:linear-gradient(135deg,#c98a52,#f4f2ee 60%,#4a5b3d)}
.feed-b{background:linear-gradient(180deg,#eae6dd,#8c6b45 50%,#3e5a2c)}
.feed-c{background:linear-gradient(180deg,#3a3d3f,#d8d6d2 60%,#2a2a2a)}
.feed-d{background:linear-gradient(180deg,#8fa6b8,#6e5a63 40%,#6c7a3a 70%,#8a6a44)}
.feed-e{background:linear-gradient(160deg,#6d8db0,#e7e6e2 45%,#5a6d43)}
.arrow{position:absolute;top:237px;width:30px;height:30px;background:var(--white);display:flex;align-items:center;justify-content:center}
.arrow.prev{left:3px}.arrow.next{right:3px}

/* Footer */
.site-footer{position:absolute;top:3540px;left:0;width:1200px;height:342px;background:var(--footer);color:#dddddd}
.footer-brand{position:absolute;left:166px;top:95px;font-family:"Fira Sans",sans-serif;font-weight:700;font-size:30px;color:var(--white);display:flex;align-items:center;gap:10px}
.footer-brand .brand-mark{background:var(--white)}
.footer-col{position:absolute;top:54px}
.footer-col h4{font-size:12px;font-weight:700;letter-spacing:.6px;color:var(--white);margin-bottom:26px}
.footer-menu{left:477px}
.footer-menu ul{list-style:none}
.footer-menu li{font-size:11.5px;line-height:20px}
.footer-contact{left:660px}
.footer-follow{left:961px}
.footer-item{display:flex;align-items:center;gap:14px;font-size:11.5px;line-height:15px;margin-bottom:21px}
.footer-item .circle{width:24px;height:24px;border-radius:50%;background:var(--white);flex:none;display:flex;align-items:center;justify-content:center}
.copyright{position:absolute;bottom:21px;width:100%;text-align:center;font-size:9.5px;color:#cccccc}
</style>
</head>
<body>

<header class="site-header">
  <div class="brand"><span class="brand-mark"></span>Hearthside Events</div>
  <div class="follow">FOLLOW US
    <span class="social-dot"></span><span class="social-dot sky"></span><span class="social-dot navy"></span>
  </div>
  <div class="call">
    <svg width="28" height="28" viewBox="0 0 28 28"><circle cx="14" cy="14" r="12.5" fill="none" stroke="#1d1d1d" stroke-width="1.6"/><path d="M10 8.5l2.3 2.6-1.2 1.6c.8 1.7 2 2.9 3.7 3.7l1.6-1.2 2.6 2.3-1.2 1.8c-4.6-.4-8.6-4.4-9-9z" fill="#1d1d1d"/></svg>
    <div class="call-text"><small>CALL US</small><strong>555.014.2290</strong></div>
  </div>
  <nav class="main-nav">
    <span class="active">HOME</span><span>ABOUT US</span><span>SERVICES</span><span>RENTAL</span><span>FAQ</span><span>CONTACT US</span>
  </nav>
</header>

<section class="hero">
  <div class="photo" role="img" aria-label="Event trailer with covered porch, tent canopy and hanging lanterns beside a house"></div>
  <form class="booking">
    <h2 class="heading" style="color:var(--white)">EVENT PLANNING</h2>
    <div class="field-row"><div class="field">FIRST NAME</div><div class="field">LAST NAME</div></div>
    <div class="field">PHONE</div>
    <div class="field">EMAIL ADDRESS</div>
    <div class="field">DATE REQUEST</div>
    <div class="btn">CHECK AVAILABILITY</div>
  </form>
  <div class="dots"><span></span><span></span><span class="on"></span><span></span><span></span></div>
</section>

<section class="welcome">
  <div class="welcome-copy">
    <div class="eyebrow">WELCOME TO</div>
    <h1 class="heading">Hearthside Events!</h1>
    <div class="rule"></div>
    <p>We provide everything you need to host any event desired!! Our goal is to provide an atmosphere that will blow away the competition and leave you feeling that you hosted an event which will leave everyone talking!!</p>
    <p>We are event planners who will provide all the goods and bring new ideas to the table that have never been done before! Starting with our main attraction the Hearthside entertainment trailer which was just completed last summer!</p>
    <span class="btn">READ MORE</span>
  </div>
  <div class="photo" role="img" aria-label="Trailer porch with wooden bar, white posts and hanging lanterns"></div>
</section>

<section class="rental">
  <h2 class="section-title heading">OUR RENTAL</h2>
  <div class="mini-rule"></div>
  <div class="rental-grid">
    <article class="rental-card">
      <div class="photo ph-trailer" role="img" aria-label="Entertainment trailer with canopy, barrels and round tables"></div>
      <h3 class="heading">FULL ENTERTAINMENT TRAILER RENTAL</h3>
      <p>For the price of $1135.00 we will deliver the trailer within 30 miles for no additional fee.</p>
      <span class="btn">READ MORE</span>
    </article>
    <article class="rental-card">
      <div class="photo ph-barrels" role="img" aria-label="Rows of rustic wooden barrels under a blue sky"></div>
      <h3 class="heading">WHISKEY BARREL RENTALS</h3>
      <p style="width:360px">Our stained Rustic Whiskey/wine barrels are $35 a piece and provide a nice touch to the rustic farmhouse style trailer.</p>
      <span class="btn">READ MORE</span>
    </article>
    <article class="rental-card">
      <div class="photo ph-tent" role="img" aria-label="Large white event tent glowing at night"></div>
      <h3 class="heading">TENT SETUP</h3>
      <p style="width:320px">Tents which are connected to the side of the trailer are rented in 12 foot sections.</p>
      <span class="btn">READ MORE</span>
    </article>
    <article class="rental-card">
      <div class="photo ph-lights" role="img" aria-label="Trailer porch with string lights under the canopy"></div>
      <h3 class="heading">LIGHTING RENTAL AND SETUP</h3>
      <p>We have classic restaurant style patio lights we hang inside and along the tent.</p>
      <span class="btn">READ MORE</span>
    </article>
  </div>
</section>

<section class="packages">
  <div class="photo" role="img" aria-label="Covered patio with round tables, white linens, chairs and barrels"></div>
  <div class="packages-copy">
    <h2 class="heading">TABLE AND CHAIR PACKAGES</h2>
    <div class="rule"></div>
    <ul class="package-list">
      <li>4- 60 inch Round tables with 32 chairs and 4 white Linens. <strong>$160 .00</strong></li>
      <li>6- 60 inch Round tables with 48 chairs and 6 white Linens. <strong>$240 .00</strong></li>
      <li>8- 60 inch Round tables with 64 chairs and 8 white Linens. <strong>$320 .00</strong></li>
      <li>10- 60 inch Round tables with 80 chairs and 10 white Linens. <strong>$400 .00</strong></li>
      <li>12- 60 inch Round tables with 96 chairs and 12 white Linens. <strong>$480 .00</strong></li>
    </ul>
  </div>
</section>

<section class="faq" role="img" aria-label="Dimmed backdrop of the trailer beside a house">
  <h2 class="section-title heading">FAQ</h2>
  <div class="mini-rule"></div>
  <div class="faq-card">
    <h3 class="heading">HOW DOES THE TRAILER HAVE LIGHTING AND WATER?</h3>
    <p>During the setup process of the Hearthside entertainment trailer we will connect a black garden hose to the closest connection available and we will run a power cord connection from the trailer to a typical common 110 volt outlet. Most likely these will run across the driveway or an area your guests will be walking so we will include a plastic yellow safety protector for the cord and hose to run through making it safe for guests to walk over.</p>
  </div>
</section>

<section class="photo-feed">
  <h2 class="section-title heading">PICTURELY</h2>
  <div class="feed-strip">
    <div class="photo feed-a" role="img" aria-label="Side of the wooden trailer parked in a driveway"></div>
    <div class="photo feed-b" role="img" aria-label="Trailer steps and porch on the lawn"></div>
    <div class="photo feed-c" role="img" aria-label="Indoor room set with round tables and sunflowers"></div>
    <div class="photo feed-d" role="img" aria-label="Patio umbrella over a barrel table"></div>
    <div class="photo feed-e" role="img" aria-label="Tent canopy with tables in a wooded yard"></div>
  </div>
  <div class="arrow prev"><svg width="10" height="14" viewBox="0 0 10 14"><path d="M8 1L2 7l6 6" fill="none" stroke="#1d1d1d" stroke-width="2"/></svg></div>
  <div class="arrow next"><svg width="10" height="14" viewBox="0 0 10 14"><path d="M2 1l6 6-6 6" fill="none" stroke="#1d1d1d" stroke-width="2"/></svg></div>
</section>

<footer class="site-footer">
  <div class="footer-brand"><span class="brand-mark"></span>Hearthside Events</div>
  <div class="footer-col footer-menu">
    <h4>MENU</h4>
    <ul><li>HOME</li><li>ABOUT US</li><li>SERVICES</li><li>RENTAL</li><li>FAQ</li><li>CONTACT US</li></ul>
  </div>
  <div class="footer-col footer-contact">
    <h4>CONTACT US</h4>
    <div class="footer-item"><span class="circle"><svg width="10" height="13" viewBox="0 0 10 13"><path d="M5 0a5 5 0 0 1 5 5c0 3.5-5 8-5 8S0 8.5 0 5a5 5 0 0 1 5-5z" fill="#262626"/><circle cx="5" cy="5" r="1.8" fill="#fff"/></svg></span><span>220 Maple Hollow Road<br>Westfield, MA 01085</span></div>
    <div class="footer-item"><span class="circle"><svg width="12" height="12" viewBox="0 0 12 12"><path d="M2 1l2.3 2.6-1 1.4c.8 1.6 1.9 2.7 3.5 3.5l1.4-1L11 9.8 9.9 11.5C5.4 11.1 1.5 7.2 1 2.6z" fill="#262626"/></svg></span><span>Call Us<br>555.014.2290</span></div>
    <div class="footer-item"><span class="circle"><svg width="12" height="9" viewBox="0 0 12 9"><rect width="12" height="9" fill="#262626"/><path d="M0 0l6 5 6-5" fill="none" stroke="#fff" stroke-width="1"/></svg></span><span>E mail Us<br>hello@hearthsideevents.com</span></div>
  </div>
  <div class="footer-col footer-follow">
    <h4>FOLLOW US</h4>
    <div class="footer-item"><span class="circle"></span><span>Like us on<br>FRIENDLINK</span></div>
    <div class="footer-item"><span class="circle"></span><span>Follow us on<br>CHIRPER</span></div>
    <div class="footer-item"><span class="circle"></span><span>Follow us on<br>WORKNET</span></div>
  </div>
  <div class="copyright">Copyright © 2021 All Rights Reserved</div>
</footer>

</body>
</html>
```